Business Card design for a skin clinic

i would like a business card design for our skin clinic.
our logo colors are Blue and Grey and Bule /white.
we are searching for a minimalistic design yet very elegant,dynamic and professional which can reflect a professional medical skin care clinic( not a beauty salon).
THE DESGIN IS NOT FOR A PERSON IT WILL BE USED IN THE CLINIC FOR CLIENTS SO THERE SHOULD BE NO NAME OF A PERSON ONLY THE CLINIC NAME AND THE CONTACT INFO

Target Market(s)
young and old womens
Industry/Entity Type
Business
Contact Information for Business Card
we have 2 address and both should be on the card.
address A: Lindenhoflaan 214B, 3041KP Rotterdam, Tel 010 483 21 95
address B: Zonnewijzerstraat 238, 1062RT Amsterdam Tel 020 571 3829
website www.huidpuntzorg.nu, email info@huidpuntzorg.nu
Look and feel
Each slider illustrates characteristics of the customer's brand and the style your logo design should communicate.

```html
<!DOCTYPE html>
<html lang="nl">
<head>
<meta charset="utf-8">
<title>Huidpuntzorg – visitekaartje</title>
<link rel="stylesheet" href="https://fonts.googleapis.com/css2?family=Montserrat:wght@300;400&display=swap">
<style>
  :root {
    --bg: #d6d7d9;
    --paper: #f4f4f3;
    --ink-dark: #1f1f20;
    --brand-blue: #3d72b8;
    --text-grey: #8a8b8d;
    --line-grey: #b5b6b8;
    --url-grey: #9a9b9d;
    --url-light: #eeeeee;
  }
  html, body {
    margin: 0;
    padding: 0;
    width: 1200px;
    height: 900px;
    overflow: hidden;
    background: var(--bg);
    font-family: "Montserrat", sans-serif;
  }
  .sheet {
    width: 1200px;
    height: 900px;
    display: flex;
    align-items: center;
    justify-content: center;
    gap: 40px;
  }
  .card {
    position: relative;
    width: 520px;
    height: 330px;
    box-sizing: border-box;
    box-shadow: 0 6px 18px rgba(0,0,0,0.15);
  }
  .card--front {
    background: var(--paper);
  }
  .card--back {
    background: var(--ink-dark);
  }

  /* front: brand */
  .brand {
    position: absolute;
    left: 44px;
    bottom: 62px;
  }
  .brand__name {
    margin: 0;
    font-weight: 400;
    font-size: 30px;
    letter-spacing: 1.5px;
    color: var(--brand-blue);
    line-height: 1;
  }
  .brand__tagline {
    margin: 8px 0 0 46px;
    font-weight: 300;
    font-size: 12px;
    letter-spacing: 0.6px;
    color: var(--text-grey);
  }

  /* front: contact column */
  .contact {
    position: absolute;
    left: 300px;
    top: 48px;
    font-weight: 300;
    font-size: 13px;
    line-height: 19px;
    color: var(--text-grey);
  }
  .contact p {
    margin: 0;
  }
  .contact .tel {
    color: var(--brand-blue);
  }
  .contact .divider {
    width: 12px;
    height: 1px;
    background: var(--line-grey);
    margin: 10px 0 9px;
  }

  /* back */
  .web {
    position: absolute;
    right: 54px;
    bottom: 78px;
    margin: 0;
    font-weight: 400;
    font-size: 12px;
    letter-spacing: 3.5px;
    color: var(--url-light);
  }
  .web__prefix {
    color: var(--url-grey);
  }
</style>
</head>
<body>
  <main class="sheet">
    <section class="card card--front" aria-label="Voorkant visitekaartje">
      <div class="brand">
        <h1 class="brand__name">HUIDPUNTZORG</h1>
        <p class="brand__tagline">next generation skin care</p>
      </div>
      <div class="contact">
        <p>Zonnewijzerstraat 238</p>
        <p>1062RT Amsterdam</p>
        <p class="tel">Tel : 020 571 3829</p>
        <div class="divider"></div>
        <p>Lindenhoflaan 214B</p>
        <p>3041KP Rotterdam</p>
        <p class="tel">Tel : 010 483 21 95</p>
        <div class="divider"></div>
        <p>info@huidpuntzorg.nu</p>
      </div>
    </section>

    <section class="card card--back" aria-label="Achterkant visitekaartje">
      <p class="web"><span class="web__prefix">www.</span>HUIDPUNTZORG.nu</p>
    </section>
  </main>
</body>
</html>
```